Real Estate Website

I am looking for a website design for a website that will be featuring real estate listings across Australia. It will be a website for a real estate agency that operates through all states in Australia.

We like the designs of https://www.brightvaleliving.com.au/ and https://velomira.asia/

On the lifestyle website, we like the sell, buy, sold tabs but would also like lease, and agents. We also need a button somewhere for 'Join Agent Horvex' and 'Login'

On the Velomira site it has a concierge section and we want something like that on the home page.

The contact details to show in the footer are:

Shop 2147B
Level 1 Coralgate Plaza Shopping Centre
87 Tidewell Crescent
Kelmarsh Bay

Attached are various versions of the logo and some intro text to go on the home page.

```html
<!DOCTYPE html>
<html lang="en">
<head>
<meta charset="utf-8">
<title>Horvex — Australia's Real Estate Hub</title>
<link href="https://fonts.googleapis.com/css2?family=Jost:wght@400;500&family=Roboto:wght@400;500;700&display=swap" rel="stylesheet">
<style>
:root{
  --gold:#b89b5e;
  --gold-light:#d6bd84;
  --gold-dark:#9c7f45;
  --navy:#0b1322;
  --ink:#1e1e1e;
  --text:#555;
  --cream:#f3e5c3;
  --footer:#1b1b1b;
  --white:#fff;
}
*{box-sizing:border-box;margin:0;padding:0}
html,body{width:1200px;height:3863px;overflow:hidden}
body{position:relative;font-family:"Roboto",sans-serif;color:var(--ink);background:var(--white)}
.abs{position:absolute}
.heading{font-family:"Jost",sans-serif;font-weight:400;text-transform:uppercase;letter-spacing:.5px}
.btn-gold{background:linear-gradient(180deg,var(--gold-light),var(--gold-dark));color:#fff;font-weight:500;text-transform:uppercase;display:flex;align-items:center;justify-content:center;border:1px solid rgba(255,255,255,.6)}
.rule{position:absolute;left:562px;width:76px;height:2px;background:var(--gold)}

/* hero */
.hero{left:0;top:0;width:1200px;height:653px;background:linear-gradient(180deg,#0a1222 0%,#1d3050 35%,#4a5a70 60%,#6b5a42 82%,#3a2e22 100%)}
.hero-header{left:0;top:0;width:1200px;height:125px;background:linear-gradient(180deg,#070d18,rgba(7,13,24,.6));border-bottom:1px solid rgba(255,255,255,.12)}
.brand{left:143px;top:52px;display:flex;align-items:center;gap:10px;font-family:"Roboto",sans-serif;font-weight:500;color:#fff;font-size:20px}
.brand i{display:block;width:18px;height:18px;border-radius:50%;background:var(--gold)}
.top-btn{top:20px;height:38px;font-size:12px}
.nav{left:564px;top:83px;display:flex;gap:30px;font-size:12.5px;font-weight:700;color:#fff}
.nav-active{left:562px;top:123px;width:44px;height:2px;background:#9aa4b5}
.hero-title{left:0;top:255px;width:1200px;text-align:center;color:#fff;font-size:42px;line-height:55px}
.tabs{left:431px;top:390px;display:flex;font-size:13px;color:#fff}
.tabs span{height:31px;display:flex;align-items:center;justify-content:center;border:1px solid #ccc;background:rgba(0,0,0,.55)}
.tabs .on{background:var(--gold);border-color:#e8d7ad}
.search{left:255px;top:462px;width:437px;height:45px;background:#fff;font-size:12px;padding:17px 15px;color:#333}
.estimate{left:702px;top:462px;width:243px;height:45px;font-size:14.5px}
.notch{left:560px;top:632px}

/* listings */
.section-title{left:0;width:1200px;text-align:center;font-size:40px;color:var(--ink)}
.card{width:300px;height:327px;background:#fff;border:2px solid #e3e3e3}
.card.raised{box-shadow:0 4px 14px rgba(0,0,0,.15)}
.card-photo{position:absolute;left:9px;top:9px;width:280px;height:177px;background:linear-gradient(180deg,#7ea6d6 0%,#c9d6e3 45%,#b7a98e 75%,#6f6a5a 100%)}
.tag-sale{position:absolute;left:0;top:18px;background:var(--gold);color:#fff;font-size:8px;padding:4px 8px;font-weight:700}
.tag-feat{position:absolute;right:0;bottom:6px;background:#111;color:#fff;font-size:8px;padding:5px 8px;font-weight:700}
.fav{position:absolute;right:18px;top:16px;width:24px;height:24px;border-radius:50%;background:#fff;display:flex;align-items:center;justify-content:center}
.card h3{position:absolute;left:26px;top:205px;font-size:15.5px;font-weight:500;color:#111}
.card .addr{position:absolute;left:26px;top:232px;font-size:12.5px;color:#333;display:flex;gap:8px;align-items:center}
.card .meta{position:absolute;left:26px;top:280px;font-size:10.5px;color:#333;display:flex;gap:14px;align-items:center}
.card .meta small{font-size:9px}
.view-more{left:478px;top:1303px;width:242px;height:42px;font-size:14px}

/* about */
.about{left:0;top:1434px;width:1200px;height:513px;background:linear-gradient(90deg,#8a8074 0%,#b8a88d 30%,#f2e4c1 45%,#f3e5c3 70%,#e3d2a9 100%)}
.about-photo{left:0;top:1434px;width:540px;height:513px;background:linear-gradient(90deg,#5b4f47 0%,#8a7968 45%,rgba(243,229,195,0) 100%)}
.about-title{left:549px;top:1500px;font-size:41px}
.about-rule{left:549px;top:1562px;width:76px;height:2px;background:var(--gold)}
.about-text{left:549px;top:1588px;width:496px;font-size:14.6px;line-height:26.4px;color:#555;text-align:justify}
.read-more{left:549px;top:1824px;width:138px;height:42px;font-size:14px}

/* concierge */
.concierge{left:35px;top:2140px;width:1131px;height:287px;border-radius:8px;background:linear-gradient(180deg,#1a2f52 0%,#36507a 55%,#56504a 80%,#2b2520 100%)}
.conc-left{left:141px;top:2208px;width:460px;color:#fff;font-size:21px;font-weight:700;line-height:34px}
.conc-right{left:624px;top:2210px;width:450px;color:#fff;font-size:13.5px;line-height:25.5px;font-weight:500}
.find-out{left:510px;top:2327px;width:179px;height:45px;font-size:15px;background:rgba(184,155,94,.85)}

.tile{top:2492px;height:348px;display:flex;align-items:center;justify-content:center;flex-direction:column;color:#fff;font-weight:700;font-size:26px;text-align:center;line-height:34px}
.tile-sales{left:0;width:386px;background:linear-gradient(135deg,#3c3c3c,#8d8d8d 60%,#5a5a5a)}
.tile-advice{left:400px;width:400px;background:linear-gradient(135deg,#a8987a,#6d5f4a 55%,#3e3a35)}
.tile-pm{left:813px;width:387px;background:linear-gradient(180deg,#4a4a4a,#2a2a2a 60%,#181818)}
.tile-btn{margin-top:10px;background:#000;border:1.5px solid #fff;font-size:13px;padding:9px 24px;line-height:1}

/* partners */
.partner{width:209px;height:102px;border:2px solid #ddd;border-radius:4px;background:#fff;display:flex;align-items:center;justify-content:center;gap:8px;font-family:"Roboto",sans-serif;font-weight:700;font-size:17px;color:#222}
.partner i{display:block;width:20px;height:20px;background:#222}
.partner.raised{box-shadow:0 3px 10px rgba(0,0,0,.18)}
.dots{left:576px;top:3221px;display:flex;gap:14px}
.dots b{width:6px;height:6px;border-radius:50%;background:#bbb}
.dots b:first-child{background:var(--gold)}

/* newsletter */
.newsletter{left:0;top:3293px;width:1200px;height:213px;background:linear-gradient(180deg,#9c7f45,#b89b5e 40%,#a88c52 70%,#5e4c2a)}
.news-title{left:143px;top:3350px;font-size:40px;line-height:51px;color:#fff}
.field{top:3378px;height:44px;background:#fff;font-size:12px;padding:15px 26px;color:#333}
.subscribe{left:915px;top:3378px;width:140px;height:44px;font-size:15px}

/* footer */
.footer{left:0;top:3506px;width:1200px;height:357px;background:var(--footer)}
.foot-brand{left:230px;top:3630px;display:flex;align-items:center;gap:12px;font-family:"Roboto",sans-serif;font-weight:500;color:#fff;font-size:28px}
.foot-brand i{display:block;width:26px;height:26px;border-radius:50%;background:var(--gold)}
.vline{width:2px;background:#444;top:3575px;height:150px}
.vline::before{content:"";position:absolute;left:0;top:0;width:2px;height:20px;background:var(--gold)}
.foot-h{top:3568px;color:#fff;font-size:17px;font-weight:500}
.foot-list{font-size:12px;color:#fff;line-height:21px}
.bottom-bar{left:0;top:3750px;width:1200px;height:113px;border-top:1px solid #333}
.copyright{left:165px;top:3804px;font-size:12px;color:#fff}
.social{top:3797px;display:flex;align-items:center;gap:6px}
.social i{width:27px;height:27px;border-radius:50%;border:2px solid var(--gold);display:block}
</style>
</head>
<body>

<!-- HERO -->
<div class="abs hero" role="img" aria-label="Photo of a modern two-storey house at dusk with lit windows"></div>
<div class="abs hero-header"></div>
<div class="abs brand"><i></i>Horvex</div>
<div class="abs top-btn btn-gold" style="left:816px;width:152px">JOIN AGENT HORVEX</div>
<div class="abs top-btn" style="left:976px;width:80px;border:1.5px solid #ccc;color:#fff;font-weight:700;display:flex;align-items:center;justify-content:center;border-radius:3px">LOGIN</div>
<nav class="abs nav"><span>HOME</span><span>BUY</span><span>SELL</span><span>LEASE</span><span>SOLD</span><span>AGENTS</span><span>CONCIERGE</span></nav>
<div class="abs nav-active"></div>
<h1 class="abs hero-title heading">Australia’s Real Estate Hub.<br>From Suburb to Skyline</h1>
<div class="abs tabs"><span class="on" style="width:68px">SELL</span><span style="width:68px">BUY</span><span style="width:68px">RENT</span><span style="width:68px">LEASE</span><span style="width:68px">AGENTS</span></div>
<div class="abs search">Start Typing to find your address</div>
<div class="abs estimate btn-gold">GET PROPERTY ESTIMATE</div>
<svg class="abs notch" width="80" height="22" viewBox="0 0 80 22"><path d="M0 22 Q40 -6 80 22Z" fill="#fff"/><path d="M34 8 l6 5 6-5" stroke="#bbb" stroke-width="1.5" fill="none"/></svg>

<!-- FEATURED LISTINGS -->
<h2 class="abs section-title heading" style="top:738px">Featured Listings</h2>
<div class="rule" style="top:798px"></div>

<div class="abs card" style="left:-40px;top:853px">
  <div class="card-photo" role="img" aria-label="Photo of modern townhouses"><span class="tag-sale">FOR SALE</span><span class="tag-feat">FEATURED</span><span class="fav"><svg width="12" height="11" viewBox="0 0 12 11"><path d="M6 10 1 5a2.8 2.8 0 015-3 2.8 2.8 0 015 3z" fill="none" stroke="#999"/></svg></span></div>
  <h3>EQUE PORRO QUISQUAM</h3>
  <div class="addr"><svg width="13" height="10"><path d="M1 2l3-1 4 1.5 4-1.5v7l-4 1.5-4-1.5-3 1z" fill="none" stroke="#b89b5e"/></svg>233,ui dolorem ipsum quia dolor sit</div>
  <div class="meta"><span>▬ 3</span><span>▙ 4</span><span>✎ 229m² <small>Offers Over $545,000</small></span></div>
</div>

<div class="abs card raised" style="left:291px;top:909px">
  <div class="card-photo" role="img" aria-label="Photo of a white house with a lawn path"><span class="tag-sale">FOR SALE</span><span class="tag-feat">FEATURED</span><span class="fav"><svg width="12" height="11" viewBox="0 0 12 11"><path d="M6 10 1 5a2.8 2.8 0 015-3 2.8 2.8 0 015 3z" fill="#e02020"/></svg></span></div>
  <h3>EQUE PORRO QUISQUAM</h3>
  <div class="addr"><svg width="13" height="10"><path d="M1 2l3-1 4 1.5 4-1.5v7l-4 1.5-4-1.5-3 1z" fill="none" stroke="#b89b5e"/></svg>233,ui dolorem ipsum quia dolor sit</div>
  <div class="meta"><span>▬ 3</span><span>▙ 4</span><span>✎ 229m² <small>Offers Over $545,000</small></span></div>
</div>

<div class="abs card" style="left:610px;top:853px">
  <div class="card-photo" role="img" aria-label="Photo of a house with a pool"><span class="tag-sale">FOR SALE</span><span class="tag-feat">FEATURED</span><span class="fav"><svg width="12" height="11" viewBox="0 0 12 11"><path d="M6 10 1 5a2.8 2.8 0 015-3 2.8 2.8 0 015 3z" fill="none" stroke="#999"/></svg></span></div>
  <h3>EQUE PORRO QUISQUAM</h3>
  <div class="addr"><svg width="13" height="10"><path d="M1 2l3-1 4 1.5 4-1.5v7l-4 1.5-4-1.5-3 1z" fill="none" stroke="#b89b5e"/></svg>233,ui dolorem ipsum quia dolor sit</div>
  <div class="meta"><span>▬ 3</span><span>▙ 4</span><span>✎ 229m² <small>Offers Over $545,000</small></span></div>
</div>

<div class="abs card" style="left:930px;top:909px">
  <div class="card-photo" role="img" aria-label="Photo of a modern house at dusk"><span class="tag-sale">FOR SALE</span><span class="tag-feat">FEATURED</span><span class="fav"><svg width="12" height="11" viewBox="0 0 12 11"><path d="M6 10 1 5a2.8 2.8 0 015-3 2.8 2.8 0 015 3z" fill="none" stroke="#999"/></svg></span></div>
  <h3>EQUE PORRO QUISQUAM</h3>
  <div class="addr"><svg width="13" height="10"><path d="M1 2l3-1 4 1.5 4-1.5v7l-4 1.5-4-1.5-3 1z" fill="none" stroke="#b89b5e"/></svg>233,ui dolorem ipsum quia dolor sit</div>
  <div class="meta"><span>▬ 3</span><span>▙ 4</span><span>✎ 229m² <small>Offers Over $545,000</small></span></div>
</div>

<div class="abs view-more btn-gold">VIEW MORE LISTINGS</div>

<!-- ABOUT -->
<div class="abs about" role="img" aria-label="Faint apartment building backdrop in cream tones"></div>
<div class="abs about-photo" role="img" aria-label="Photo of an agent shaking hands with a couple outside a home"></div>
<h2 class="abs about-title heading">About Us</h2>
<div class="abs about-rule"></div>
<p class="abs about-text">Sed ut perspiciatis unde omnis iste natus error sit voluptatem accusantium doloremque laudantium, totam rem aperiam, eaque ipsa quae ab illo inventore veritatis et quasi architecto beatae vitae dicta sunt explicabo. Nemo enim ipsam voluptatem quia voluptas sit aspernatur aut odit aut fugit, sed quia consequuntur magni dolores eos qui ratione voluptatem sequi nesciunt. Neque porro quisquam est, qui dolorem ipsum quia dolor sit amet, consectetur, adipisci velit, sed quia non numquam eius modi tempora incidunt ut labore et dolore magnam aliquam quaerat voluptatem.</p>
<div class="abs read-more btn-gold">READ MORE</div>

<!-- CONCIERGE -->
<h2 class="abs section-title heading" style="top:2042px">Agent Horvex Concierge</h2>
<div class="rule" style="top:2104px"></div>
<div class="abs concierge" role="img" aria-label="Photo of a row of homes at dusk under a blue sky"></div>
<p class="abs conc-left">Looking buy, rent or sell something unique? Want competitive developer financing at great rates?</p>
<p class="abs conc-right">Agent Horvex can help you find, buy, rent or sell unique properties through our extensive global agent network and assist with financing at competitive rates with fast approvals.</p>
<div class="abs find-out btn-gold">FIND OUT MORE</div>

<div class="abs tile tile-sales" role="img" aria-label="Photo of a couple holding new house keys"><span>SALES</span></div>
<div class="abs tile tile-advice" role="img" aria-label="Photo of an agent advising a couple in a kitchen"><span style="margin-top:60px">ADVICE</span><span class="tile-btn">FIND OUT MORE</span></div>
<div class="abs tile tile-pm" role="img" aria-label="Photo of a modern house with a pool at night"><span>PROPERTY<br>MANAGEMENT</span></div>

<!-- PARTNERS -->
<h2 class="abs section-title heading" style="top:2917px">Our Partners</h2>
<div class="rule" style="top:2979px"></div>
<div class="abs partner" style="left:32px;top:3042px"><i></i>NORTHMARK</div>
<div class="abs partner" style="left:263px;top:3075px"><i style="border-radius:50%"></i>Quillstone</div>
<div class="abs partner raised" style="left:495px;top:3042px;flex-direction:column;gap:2px"><span style="font-size:25px">Brightpage</span><span style="font-size:7px;font-weight:400">A Paperline Brand</span></div>
<div class="abs partner" style="left:726px;top:3075px"><i></i>Keystrand</div>
<div class="abs partner" style="left:959px;top:3042px"><i style="border-radius:50%"></i>Tallowbay</div>
<div class="abs dots"><b></b><b></b><b></b></div>

<!-- NEWSLETTER -->
<div class="abs newsletter" role="img" aria-label="Gold-toned photo of a harbour bridge and city"></div>
<h2 class="abs news-title heading">Subscribe to<br>Newsletter</h2>
<div class="abs field" style="left:443px;width:225px">Enter Name</div>
<div class="abs field" style="left:678px;width:227px">Enter Email</div>
<div class="abs subscribe btn-gold">SUBSCRIBE</div>

<!-- FOOTER -->
<footer class="abs footer"></footer>
<div class="abs foot-brand"><i></i>Horvex</div>
<div class="abs vline" style="left:532px"></div>
<div class="abs foot-h" style="left:560px">CONTACT</div>
<svg class="abs" style="left:559px;top:3613px" width="9" height="12" viewBox="0 0 9 12"><path d="M4.5 12S0 7 0 4.5a4.5 4.5 0 019 0C9 7 4.5 12 4.5 12z" fill="#b89b5e"/><circle cx="4.5" cy="4.5" r="1.6" fill="#1b1b1b"/></svg>
<div class="abs foot-list" style="left:580px;top:3609px">Shop 2147B<br>Level 1 Coralgate Plaza Shopping Centre<br>87 Tidewell Crescent<br>Kelmarsh Bay</div>
<div class="abs vline" style="left:865px"></div>
<div class="abs foot-h" style="left:901px">LINKS</div>
<div class="abs foot-list" style="left:902px;top:3609px">Buy<br>Sell<br>Lease<br>Sold</div>
<div class="abs foot-list" style="left:959px;top:3609px">Agents<br>Concierge</div>
<div class="abs bottom-bar"></div>
<div class="abs copyright">© 2025 Agent Horvex.All Rights Reserved &nbsp;|&nbsp; Privacy Policy &nbsp;|&nbsp; Cookie Policy &nbsp;|&nbsp; Disclaimer &nbsp;|&nbsp; Trade Marks &amp; Legal</div>
<div class="abs social" style="left:932px" aria-label="Social links: Pixora, Folkly, Chirpo"><i></i><i></i><i></i></div>

</body>
</html>
```